Zorvo Salsa label for 16oz jar

We need a design for a label for a 16oz glass jar for salsa (dimensions in inches- 2.75 x9.5). Name of salsa is “Zorvo Salsa” and needs to include a place for medium or hot for the different flavors. Looking for bright Fiesta colors but a mature look. Attached is an image of the coloring scheme we like. There will need to be nutrition facts on one end and a description of the product/flavor on the other side of the label. Ultimately at this point looking for brand design.

```html
<!DOCTYPE html>
<html lang="en">
<head>
<meta charset="utf-8">
<title>Zorvo Salsa – Label Variants</title>
<link href="https://fonts.googleapis.com/css2?family=Rye&family=Open+Sans+Condensed:wght@700&display=swap" rel="stylesheet">
<style>
  :root {
    --bg: #ebe7e1;
    --purple: #8e1f86;
    --purple-dark: #6d1567;
    --red: #c8231c;
    --red-dark: #9c1713;
    --deep-red: #a8181d;
    --deep-red-dark: #7f1014;
    --gold: #f1b51c;
    --gold-soft: #e9a21a;
    --chili: #e0402a;
    --cream: #f6f1e6;
  }
  html, body {
    margin: 0;
    width: 1200px;
    height: 675px;
    overflow: hidden;
    background: var(--bg);
  }
  .lineup {
    position: absolute;
    left: 45px;
    top: 222px;
    display: flex;
    gap: 30px;
  }
  .label {
    --base: var(--red);
    --shade: var(--red-dark);
    position: relative;
    width: 350px;
    height: 230px;
    overflow: hidden;
    background: var(--base);
  }
  .label--purple { --base: var(--purple); --shade: var(--purple-dark); }
  .label--red { --base: var(--red); --shade: var(--red-dark); }
  .label--deep-red { --base: var(--deep-red); --shade: var(--deep-red-dark); }

  .label__border {
    position: absolute;
    left: 0;
    right: 0;
    height: 12px;
    background: var(--gold);
    border-top: 2px solid var(--shade);
    border-bottom: 2px solid var(--shade);
  }
  .label__border--top { top: 6px; }
  .label__border--bottom { bottom: 6px; }

  .label__ornament {
    position: absolute;
    top: 30px;
    bottom: 30px;
    width: 104px;
    border-radius: 6px;
  }
  .label__ornament--left {
    left: 6px;
    background: linear-gradient(135deg, var(--gold-soft) 0%, var(--chili) 50%, var(--shade) 100%);
  }
  .label__ornament--right {
    right: 6px;
    background: linear-gradient(225deg, var(--gold-soft) 0%, var(--chili) 50%, var(--shade) 100%);
  }

  .label__brand {
    position: absolute;
    left: 112px;
    right: 112px;
    top: 36px;
    text-align: center;
    color: var(--cream);
    font-family: "Rye", serif;
    line-height: 1;
  }
  .brand__name {
    font-size: 38px;
    margin: 0;
    font-weight: 400;
  }
  .brand__name span { display: block; }
  .brand__name span + span { margin-top: 2px; }
  .label__flavor {
    margin-top: 8px;
    font-family: "Rye", serif;
    font-size: 20px;
    color: var(--gold);
  }
  .label--deep-red .label__flavor { color: #ec4a2c; }
  .label__weight {
    margin-top: 6px;
    font-family: "Open Sans Condensed", "Arial Narrow", sans-serif;
    font-weight: 700;
    font-size: 9px;
    letter-spacing: 0.3px;
    color: var(--cream);
    white-space: nowrap;
  }
</style>
</head>
<body>
  <main class="lineup">
    <section class="label label--purple">
      <div class="label__border label__border--top" role="img" aria-label="Gold zigzag triangle border"></div>
      <div class="label__ornament label__ornament--left" role="img" aria-label="Gold and red swirl ornament with chili peppers"></div>
      <div class="label__ornament label__ornament--right" role="img" aria-label="Gold and red swirl ornament with chili peppers"></div>
      <div class="label__brand">
        <h1 class="brand__name"><span>Zorvo</span><span>Salsa</span></h1>
        <div class="label__flavor">Hot</div>
        <div class="label__weight">NET WT 16 OZ 439g</div>
      </div>
      <div class="label__border label__border--bottom" role="img" aria-label="Gold zigzag triangle border"></div>
    </section>

    <section class="label label--red">
      <div class="label__border label__border--top" role="img" aria-label="Gold zigzag triangle border"></div>
      <div class="label__ornament label__ornament--left" role="img" aria-label="Gold and red swirl ornament with chili peppers"></div>
      <div class="label__ornament label__ornament--right" role="img" aria-label="Gold and red swirl ornament with chili peppers"></div>
      <div class="label__brand">
        <h1 class="brand__name"><span>Zorvo</span><span>Salsa</span></h1>
        <div class="label__flavor">Hot</div>
        <div class="label__weight">NET WT 16 OZ 439g</div>
      </div>
      <div class="label__border label__border--bottom" role="img" aria-label="Gold zigzag triangle border"></div>
    </section>

    <section class="label label--deep-red">
      <div class="label__border label__border--top" role="img" aria-label="Gold zigzag triangle border"></div>
      <div class="label__ornament label__ornament--left" role="img" aria-label="Gold and red swirl ornament with chili peppers"></div>
      <div class="label__ornament label__ornament--right" role="img" aria-label="Gold and red swirl ornament with chili peppers"></div>
      <div class="label__brand">
        <h1 class="brand__name"><span>Zorvo</span><span>Salsa</span></h1>
        <div class="label__flavor">Hot</div>
        <div class="label__weight">NET WT 16 OZ 439g</div>
      </div>
      <div class="label__border label__border--bottom" role="img" aria-label="Gold zigzag triangle border"></div>
    </section>
  </main>
</body>
</html>
```